Business Cards using attached files

Please make new business cards using files attached. I would like something a little more updated possibly. Double sided.
I am wanting to make sure I can change the names and positions easily myself.

Target Market(s)

Automotive Repair

Industry/Entity Type

Automotive

Contact Information for Business Card

See attached files

Font styles to use
Serif

Colors
0054AA
0677BA
7BADD7
CADEEF
E8F1F8

Requirements
Must have
• Red white blue colors
Nice to have
• I'd like it slightly updated from our existing design. Double sided. I'd like to be able to change names and positions easily to have them printed.
Should not have
• I'm not sure

```html
<!DOCTYPE html>
<html lang="en">
<head>
<meta charset="utf-8">
<title>Ridgeway Auto &amp; Truck — Business Card</title>
<link href="https://fonts.googleapis.com/css2?family=Libre+Baskerville:ital,wght@0,700;1,400&family=Roboto:wght@400&display=swap" rel="stylesheet">
<style>
  :root {
    --bg: #acacac;
    --navy: #243b58;
    --navy-deep: #1c2f48;
    --steel: #3f6f9f;
    --red: #d0383d;
    --white: #ffffff;
    --ink-soft: #7a7a7a;
    --rule: #b9b9b9;
  }
  * { margin: 0; padding: 0; box-sizing: border-box; }
  html, body { width: 1200px; height: 1000px; overflow: hidden; }
  body { background: var(--bg); position: relative; font-family: "Roboto", sans-serif; }

  .card {
    position: absolute;
    left: 293px;
    width: 613px;
    height: 351px;
    border-radius: 24px;
    overflow: hidden;
    box-shadow: 0 18px 40px rgba(0,0,0,0.28);
  }
  .card--front { top: 118px; background: var(--navy); }
  .card--back { top: 530px; background: var(--white); }

  .front-pattern {
    position: absolute; inset: 0;
    background: linear-gradient(100deg, var(--navy-deep) 0%, var(--navy) 45%, var(--steel) 100%);
    opacity: 0.55;
  }

  .brand { position: absolute; display: flex; align-items: center; gap: 10px;
    font-family: "Libre Baskerville", serif; font-weight: 700; white-space: nowrap; }
  .brand__dot { width: 14px; height: 14px; border-radius: 50%; background: var(--red); flex: none; }

  .card--front .brand { right: 80px; top: 224px; color: var(--white); font-size: 22px; }
  .card--back .brand { left: 0; right: 0; top: 50px; justify-content: center; color: var(--navy); font-size: 29px; }

  .person { position: absolute; right: 335px; top: 175px; text-align: right; }
  .person__name { font-family: "Libre Baskerville", serif; font-weight: 700; font-size: 24px; color: var(--navy); line-height: 1.1; }
  .person__role { font-family: "Libre Baskerville", serif; font-style: italic; font-size: 15px; color: var(--red); margin-top: 2px; }

  .divider { position: absolute; left: 307px; top: 150px; width: 1px; height: 100px; background: var(--rule); }

  .contact { position: absolute; left: 331px; top: 170px; list-style: none;
    font-size: 17px; line-height: 21px; color: var(--ink-soft); }

  .address { position: absolute; left: 0; right: 0; top: 310px; text-align: center;
    font-size: 17px; color: var(--ink-soft); }
</style>
</head>
<body>
  <section class="card card--front">
    <div class="front-pattern" role="img" aria-label="Embossed repeating brand pattern in navy and steel blue tones"></div>
    <div class="brand"><span class="brand__dot"></span>Ridgeway Auto &amp; Truck</div>
  </section>

  <section class="card card--back">
    <div class="brand"><span class="brand__dot"></span>Ridgeway Auto &amp; Truck</div>

    <div class="person">
      <p class="person__name">Daniel Mercer</p>
      <p class="person__role">General Manager</p>
    </div>

    <div class="divider"></div>

    <ul class="contact">
      <li>(555) 014-2290</li>
      <li>service@ridgewayauto.com</li>
      <li>www.ridgewayauto.com</li>
    </ul>

    <p class="address">418 Harbor Road, Millbrook, NY 10599</p>
  </section>
</body>
</html>
```